Webdesign für Getränkelogistik & Full-Service-Partner bei Events
Zielgruppe
Getränkelogistiker und Full-Service-Partner bei Events
Zielgruppe: Getränke-EinzelHändler; Veranstalter von Events und privaten Feiern
Aufgabenstellung
- soll „Frische“ und „Moderne“ vermitteln, ohne eine Getränkeart in den Vordergrund zu rücken
- soll von den Farben her gut zum Logo passen (siehe Anlagen)
- Slider wäre wünschenswert
- Slogan 'Wir freuen uns auf Sie!'

```html
<!DOCTYPE html>
<html lang="de">
<head>
<meta charset="utf-8">
<title>Getränke Brandl GmbH</title>
<link rel="stylesheet" href="https://fonts.googleapis.com/css2?family=Open+Sans:wght@400;600;700&family=Playfair+Display:wght@400;700&display=swap">
<style>
:root{
  --green-dark:#1b5e50;
  --green-title:#226b5c;
  --yellow:#f6c200;
  --amber:#e4a800;
  --text:#3a3a3a;
  --rule:#cfcfcf;
  --hero-dark:#023a0c;
  --hero-light:#0f9a22;
}
*{margin:0;padding:0;box-sizing:border-box}
html,body{width:1146px;height:1200px;overflow:hidden;background:#fff}
body{position:relative;font-family:"Open Sans",sans-serif;color:var(--text)}
.brand{position:absolute;left:0;width:1146px;top:26px;display:flex;justify-content:center;align-items:center;gap:8px}
.brand-dot{width:26px;height:26px;border-radius:50%;background:var(--yellow)}
.brand-name{font-family:"Open Sans",sans-serif;font-weight:700;font-size:24px;color:var(--green-dark)}
.nav{position:absolute;left:222px;top:90px;width:702px;height:47px;border-top:1px solid var(--rule);border-bottom:1px solid var(--rule)}
.nav a{position:absolute;top:15px;font-size:11px;color:#555;text-decoration:none}
.nav a.active{color:var(--green-dark);font-weight:700}
.hero{position:absolute;left:140px;top:154px;width:865px;height:421px;background:radial-gradient(ellipse at 75% 55%,var(--hero-light) 0%,#0a7018 40%,var(--hero-dark) 100%)}
.hero-photo{position:absolute;right:0;top:0;width:500px;height:421px;background:linear-gradient(180deg,rgba(20,120,35,0) 0%,rgba(20,120,35,0) 72%,rgba(200,225,210,.7) 100%)}
.slogan{position:absolute;left:82px;top:124px;font-family:"Playfair Display",serif;font-size:37px;line-height:43px;color:#fff}
.thumbs{position:absolute;left:82px;top:362px;display:flex;gap:6px}
.thumb{width:42px;height:42px}
.thumb.active{outline:2px solid var(--yellow);outline-offset:-2px}
.hotline{position:absolute;left:994px;top:172px;width:152px;height:57px;background:var(--yellow);padding:9px 0 0 11px}
.hotline small{display:block;font-size:12px;color:#333;line-height:15px}
.hotline strong{display:block;font-size:19.5px;font-weight:700;color:var(--green-dark);line-height:25px}
.service{position:absolute;top:645px;width:163px}
.service-label{font-size:10.5px;font-weight:700;color:var(--yellow);letter-spacing:.3px}
.service-rule{width:30px;height:1px;background:var(--rule);margin-top:11px}
.service-title{font-family:"Playfair Display",serif;font-weight:700;font-size:23px;color:var(--green-title);margin-top:15px;margin-left:-1px}
.service-text{font-size:10.5px;line-height:16.5px;margin-top:20px;height:66px}
.service-photo{display:block;width:162px;height:111px;margin-top:14px}
.more{display:block;text-align:right;margin-top:14px;font-size:11px;font-weight:700;color:var(--green-title);text-decoration:underline}
.beer-band{position:absolute;left:0;top:1000px;width:1146px;height:200px;background:linear-gradient(180deg,rgba(255,255,255,0) 0%,rgba(246,194,0,.55) 22%,var(--amber) 45%,var(--yellow) 100%)}
.footer-links{position:absolute;left:222px;top:1162px;font-size:10.5px;font-weight:600;color:#222}
.footer-links a{color:#222;text-decoration:none}
.footer-links span{margin:0 6px}
</style>
</head>
<body>
<header class="brand">
  <div class="brand-dot"></div>
  <div class="brand-name">Getränke Brandl GmbH</div>
</header>

<nav class="nav">
  <a class="active" style="left:83px">Home</a>
  <a style="left:144px">Unternehmen</a>
  <a style="left:243px">Team</a>
  <a style="left:302px">Großhandel</a>
  <a style="left:390px">Rund um Ihr Event</a>
  <a style="left:512px">Karriere</a>
  <a style="left:581px">Kontakt</a>
</nav>

<section class="hero">
  <div class="hero-photo" role="img" aria-label="Zwei grüne Glasflaschen mit Wassertropfen in Eiswürfeln"></div>
  <p class="slogan">“Wir freuen uns<br>auf Sie!”</p>
  <div class="thumbs">
    <div class="thumb active" role="img" aria-label="Vorschau grüne Flaschen" style="background:linear-gradient(135deg,#034010,#0e8a1f)"></div>
    <div class="thumb" role="img" aria-label="Vorschau Feier mit Gläsern" style="background:linear-gradient(135deg,#f0c8b0,#c0282a)"></div>
    <div class="thumb" role="img" aria-label="Vorschau Weingläser" style="background:linear-gradient(135deg,#3a1a10,#c0602a)"></div>
    <div class="thumb" role="img" aria-label="Vorschau Erfrischungsgetränke" style="background:linear-gradient(135deg,#8fd0e8,#f0a030)"></div>
  </div>
</section>

<aside class="hotline">
  <small>Bestell-Hotline:</small>
  <strong>037200 45190</strong>
</aside>

<div class="beer-band" role="img" aria-label="Goldgelbe Getränkeoberfläche mit Schaum als Seitenabschluss"></div>

<article class="service" style="left:222px">
  <div class="service-label">SERVICE 01</div>
  <div class="service-rule"></div>
  <h2 class="service-title">Für Ihr Event</h2>
  <p class="service-text">Dies ist ein Typoblindtext. An ihm kann man sehen, ob alle Buchstaben da sind und wie sie aussehen.</p>
  <div class="service-photo" role="img" aria-label="Festzelt mit geschmückten Stühlen im Freien" style="background:linear-gradient(180deg,#2a3cb0,#e8e8f0 60%,#6a8a50)"></div>
  <a class="more">weiterlesen</a>
</article>

<article class="service" style="left:402px">
  <div class="service-label">SERVICE 02</div>
  <div class="service-rule"></div>
  <h2 class="service-title">Großhandel</h2>
  <p class="service-text">Dies ist ein Typoblindtext. An ihm kann man sehen, ob alle Buchstaben da sind und wie sie aussehen.</p>
  <div class="service-photo" role="img" aria-label="Grüne Lieferwagen des Getränkehandels auf dem Hof" style="background:linear-gradient(180deg,#e6e8ea,#2d6a40 50%,#7a7a7a)"></div>
  <a class="more">weiterlesen</a>
</article>

<article class="service" style="left:581px">
  <div class="service-label">SERVICE 03</div>
  <div class="service-rule"></div>
  <h2 class="service-title">Unternehmen</h2>
  <p class="service-text">Dies ist ein Typoblindtext. An ihm kann man sehen, ob alle Buchstaben da sind und wie sie aussehen.</p>
  <div class="service-photo" role="img" aria-label="Geschäftsführer am Treppengeländer" style="background:linear-gradient(135deg,#cfd3d6,#eef0f2 55%,#9aa0a5)"></div>
  <a class="more">weiterlesen</a>
</article>

<article class="service" style="left:761px">
  <div class="service-label">SERVICE 04</div>
  <div class="service-rule"></div>
  <h2 class="service-title">Team</h2>
  <p class="service-text">Dies ist ein Typoblindtext. An ihm kann man sehen, ob alle Buchstaben da sind und wie sie aussehen.</p>
  <div class="service-photo" role="img" aria-label="Das Team vor der Lagerhalle" style="background:linear-gradient(180deg,#d8d000,#3a3f3a 35%,#5a6a5a)"></div>
  <a class="more">weiterlesen</a>
</article>

<footer class="footer-links">
  <a>Downloads</a><span>|</span><a>Kontakt</a><span>|</span><a>Impressum / Datenschutz</a><span>|</span><a>AGB</a>
</footer>
</body>
</html>
```